We need a business card design for a new company based in
Perth, Western Australia called Oveko Tiling Services. We specialize in laying Wall and Floor Tiles and Stone. We expertise in all small to large format tiles and do good quality work. Sincerity and Convition is what seperates us from others.

```html
<!DOCTYPE html>
<html lang="en">
<head>
<meta charset="utf-8">
<title>Oveko Tiling Services – Business Card</title>
<link href="https://fonts.googleapis.com/css2?family=Open+Sans:wght@400;600;700&display=swap" rel="stylesheet">
<style>
  :root {
    --page-bg: #e9e9e7;
    --stone-light: #cfcfcf;
    --stone-mid: #b9b9b9;
    --stone-dark: #a8a8a8;
    --band: #5e7887;
    --band-edge: #6b9fb4;
    --accent: #a3dfe8;
    --brand-text: #e6eef1;
    --ink: #111111;
  }
  * { margin: 0; padding: 0; box-sizing: border-box; }
  html, body {
    width: 1200px; height: 1000px; overflow: hidden;
    background: var(--page-bg);
    font-family: "Open Sans", Arial, sans-serif;
  }
  .card {
    position: absolute; left: 100px; top: 210px;
    width: 1000px; height: 580px;
    overflow: hidden;
    box-shadow: 0 10px 30px rgba(0,0,0,0.25);
  }
  .card-texture {
    position: absolute; inset: 0;
    background: linear-gradient(135deg, var(--stone-light) 0%, var(--stone-mid) 55%, var(--stone-dark) 100%);
  }
  .band {
    position: absolute; left: 0; top: 80px;
    width: 1000px; height: 170px;
    background: var(--band);
    border-top: 9px solid var(--band-edge);
    border-bottom: 9px solid var(--band-edge);
  }
  .brand {
    position: absolute; left: 120px; top: 118px;
    display: flex; align-items: center; gap: 22px;
  }
  .brand-square { width: 84px; height: 84px; background: var(--accent); flex: none; }
  .brand-name {
    color: var(--brand-text); font-weight: 600;
    font-size: 34px; line-height: 1.15; letter-spacing: 3px;
    text-transform: uppercase;
  }
  .person { position: absolute; left: 540px; top: 290px; color: var(--ink); }
  .person-name { font-size: 46px; font-weight: 700; line-height: 1.1; }
  .person-role { font-size: 18px; margin-top: 6px; }
  .contact {
    position: absolute; left: 540px; top: 420px;
    list-style: none; color: var(--ink); font-size: 27px;
  }
  .contact li { display: flex; align-items: center; gap: 14px; height: 42px; white-space: nowrap; }
  .contact svg { width: 30px; height: 24px; flex: none; }
</style>
</head>
<body>
  <article class="card">
    <div class="card-texture" role="img" aria-label="Grey stone floor tile texture background"></div>
    <div class="band"></div>

    <div class="brand">
      <div class="brand-square"></div>
      <div class="brand-name">Oveko<br>Tiling Services</div>
    </div>

    <div class="person">
      <h1 class="person-name">Name Here</h1>
      <p class="person-role">Position</p>
    </div>

    <ul class="contact">
      <li>
        <svg viewBox="0 0 30 24" aria-label="Phone">
          <path d="M3 8c0-4 24-4 24 0v3h-6V8H9v3H3z" fill="#111"/>
          <path d="M7 12h16l3 10H4z" fill="#111"/>
          <circle cx="15" cy="17" r="3" fill="#c4c4c4"/>
        </svg>
        <span>000 000000</span>
      </li>
      <li>
        <svg viewBox="0 0 30 24" aria-label="Email">
          <rect x="2" y="3" width="26" height="18" fill="#111"/>
          <path d="M3 4l12 10L27 4" stroke="#c4c4c4" stroke-width="2" fill="none"/>
        </svg>
        <span>name@oveko.com.au</span>
      </li>
    </ul>
  </article>
</body>
</html>
```